New Company Brochure for Email send out

Want to have a new professional and eye catching company brochure
We are an I.T. Infrastructure solution provider

Focus Solution
1) Server Room Setup (UPS, CRAC, etc)
2) All-in-One Rack Solution (Key focus)
3) Structured Cabling and Fiber Backbone wiring
4) other solution (CCTV & Access Control Solution, Conference Room AV Solution)

Hope to have
1) total around 6 pages (including front cover and last page)
2) Suggested format : Powerpoint, word, excel or visio
3) sorry we have no knowledge on AI
Updates

Low design quality

Target Market(s)

Enterprise

Industry/Entity Type

I.T.

Requirements
Must have
• Our Product Photo (All-in-One Rack Solution, Structured Cabling, Server room Setup)
Nice to have
• Some our vendor partners logo
Should not have
• Our Existing Client Logo

```html
<!DOCTYPE html>
<html lang="en">
<head>
<meta charset="utf-8">
<title>Vantaro Data Center Infrastructure Brochure</title>
<link href="https://fonts.googleapis.com/css2?family=Arimo:wght@400;700&family=Poppins:wght@300;400;500&family=Rajdhani:wght@600;700&display=swap" rel="stylesheet">
<style>
:root{
  --teal:#0f5f6e;
  --teal-dark:#0b4d5b;
  --teal-light:#2c8592;
  --green:#1aa37a;
  --paper:#f1f3f4;
  --ink:#333a3e;
  --heading:#12606e;
  --stage:#8c8c8c;
  --muted:#5d6468;
}
*{box-sizing:border-box;margin:0;padding:0}
html,body{width:1200px;height:3011px;overflow:hidden}
body{background:var(--stage);position:relative;font-family:"Poppins",sans-serif;color:var(--ink)}
.page{position:absolute;overflow:hidden;box-shadow:0 4px 14px rgba(0,0,0,.35)}
.abs{position:absolute}
.photo{position:absolute;border-radius:10px}
.brand{position:absolute;display:flex;align-items:center;gap:8px;font-family:"Poppins",sans-serif;font-weight:500;color:var(--teal)}
.brand-mark{width:22px;height:22px;border:3px solid var(--teal);border-radius:3px}
.social{position:absolute;width:26px;height:26px;border-radius:50%;background:#fff}
.cover-year{font-family:"Arimo",sans-serif;font-weight:700;color:var(--teal-dark)}
.cover-title{font-family:"Arimo",sans-serif;font-weight:700;color:var(--teal-dark)}
.cover-by{font-family:"Arimo",sans-serif;color:var(--muted)}
.band{position:absolute;left:0;right:0;bottom:0;background:var(--teal);color:#fff;font-family:"Poppins",sans-serif;text-align:center}
.back-bg{background:linear-gradient(90deg,var(--teal-dark),var(--teal-light))}
.contact{position:absolute;color:#fff;font-family:"Arimo",sans-serif}
.contact h2{font-weight:700}
.contact h3{font-weight:700}
.label{position:absolute;color:#fff;font-family:"Poppins",sans-serif;font-weight:300;font-size:20px;transform:translateX(-50%)}
.spread{background:linear-gradient(180deg,#ffffff,var(--paper))}
.sec-title{position:absolute;font-family:"Rajdhani",sans-serif;font-weight:700;color:var(--heading);font-size:22px;line-height:1.15}
.body{position:absolute;font-size:10px;line-height:1.4;text-align:justify;color:var(--ink)}
.tile{position:absolute;width:98px;height:100px;border:3px solid var(--green);border-radius:14px;background:#fff;overflow:hidden}
.tile-fill{width:100%;height:100%}
.tile-label{position:absolute;width:120px;text-align:center;font-size:9px;line-height:1.35;color:var(--muted);text-transform:uppercase}
.footer-band{position:absolute;bottom:0;height:40px;background:var(--teal)}
.pg{position:absolute;bottom:0;width:26px;height:32px;background:#fff;font-size:14px;color:#333;display:flex;align-items:center;justify-content:center}
.url{position:absolute;bottom:12px;font-size:9px;color:#fff}
.partner{position:absolute;background:#d6dadc;border-radius:4px}
</style>
</head>
<body>

<!-- Open flat spread: back cover + front cover -->
<section class="page back-bg" style="left:150px;top:90px;width:450px;height:600px">
  <div class="contact" style="left:30px;top:300px">
    <h2 style="font-size:19px">Contact Us</h2>
    <h3 style="font-size:12px;margin-top:10px">Mail Us</h3>
    <p style="font-size:10px">hello@vantarotech.example</p>
    <h3 style="font-size:12px;margin-top:10px">Phone</h3>
    <p style="font-size:10px">(+852) 2100 4800 / (+852) 6200 3175</p>
    <h3 style="font-size:12px;margin-top:10px">Fax</h3>
    <p style="font-size:10px">(+852) 2100 4899</p>
  </div>
</section>
<section class="page" style="left:600px;top:90px;width:450px;height:600px;background:var(--paper)">
  <div class="abs" style="left:0;top:0;width:228px;height:284px;background:var(--teal)"></div>
  <div class="brand" style="left:248px;top:36px;font-size:26px"><span class="brand-mark"></span>Vantaro</div>
  <span class="social" style="left:84px;top:92px"></span>
  <span class="social" style="left:130px;top:92px"></span>
  <span class="social" style="left:176px;top:92px"></span>
  <div class="photo" role="img" aria-label="Server racks in a data center room" style="left:74px;top:160px;width:178px;height:163px;background:linear-gradient(160deg,#6b7278,#2a3035 60%,#c9cdd0);border:4px solid #fff"></div>
  <div class="photo" role="img" aria-label="Blue network cables plugged into a switch" style="left:200px;top:258px;width:174px;height:164px;background:linear-gradient(150deg,#cfe1f7,#3d7fe0 55%,#7b8fd8)"></div>
  <div class="cover-year abs" style="left:60px;top:388px;font-size:46px">2021</div>
  <div class="cover-title abs" style="left:60px;top:440px;font-size:19px">Data Center Infrastructure Solution</div>
  <div class="cover-by abs" style="left:60px;top:466px;font-size:14px">By Vantaro Technology Solutions Limited</div>
  <div class="band" style="height:45px;line-height:45px;font-size:13px">www.vantarotech.example</div>
</section>

<div class="label" style="left:367px;top:734px">Cover Page</div>
<div class="label" style="left:846px;top:734px">Back Page</div>

<!-- Front cover -->
<section class="page" style="left:123px;top:786px;width:474px;height:635px;background:var(--paper)">
  <div class="abs" style="left:0;top:0;width:239px;height:300px;background:var(--teal)"></div>
  <div class="brand" style="left:256px;top:38px;font-size:28px"><span class="brand-mark"></span>Vantaro</div>
  <span class="social" style="left:88px;top:97px"></span>
  <span class="social" style="left:138px;top:97px"></span>
  <span class="social" style="left:188px;top:97px"></span>
  <div class="photo" role="img" aria-label="Server racks in a data center room" style="left:78px;top:169px;width:188px;height:172px;background:linear-gradient(160deg,#6b7278,#2a3035 60%,#c9cdd0);border:4px solid #fff"></div>
  <div class="photo" role="img" aria-label="Blue network cables plugged into a switch" style="left:210px;top:273px;width:184px;height:173px;background:linear-gradient(150deg,#cfe1f7,#3d7fe0 55%,#7b8fd8)"></div>
  <div class="cover-year abs" style="left:76px;top:405px;font-size:50px">2021</div>
  <div class="cover-title abs" style="left:76px;top:456px;font-size:20px">Data Center Infrastructure Solution</div>
  <div class="cover-by abs" style="left:76px;top:484px;font-size:15px">By Vantaro Technology Solutions Limited</div>
  <div class="band" style="height:46px;line-height:46px;font-size:14px">www.vantarotech.example</div>
</section>

<!-- Back cover -->
<section class="page back-bg" style="left:636px;top:786px;width:476px;height:635px">
  <div class="contact" style="left:27px;top:270px">
    <h2 style="font-size:21px">Contact Us</h2>
    <h3 style="font-size:13px;margin-top:14px">Mail Us</h3>
    <p style="font-size:10.5px">hello@vantarotech.example</p>
    <h3 style="font-size:13px;margin-top:14px">Phone</h3>
    <p style="font-size:10.5px">(+852) 2100 4800 / (+852) 6200 3175</p>
    <h3 style="font-size:13px;margin-top:14px">Fax</h3>
    <p style="font-size:10.5px">(+852) 2100 4899</p>
  </div>
</section>

<!-- Spread: pages 01-02 -->
<section class="page spread" style="left:129px;top:1469px;width:971px;height:704px">
  <h2 class="sec-title" style="left:25px;top:44px">Server Room Setup (UPS)</h2>
  <p class="body" style="left:25px;top:90px;width:446px">Electricity is an invisible hero but the most critical element in running a data center. It ensures uninterrupted power for numerous servers and devices. It cleans out power sags, surges, spikes and noises; helping to prevent damage to our sensitive electronic gears.</p>

  <div class="tile" style="left:25px;top:165px"><div class="tile-fill" role="img" aria-label="Rackmount UPS unit" style="background:linear-gradient(150deg,#d8dcdf,#2d3337)"></div></div>
  <div class="tile" style="left:139px;top:165px"><div class="tile-fill" role="img" aria-label="Modular UPS front panel" style="background:linear-gradient(160deg,#3a3f42,#1c2022 60%,#6d8a4a)"></div></div>
  <div class="tile" style="left:256px;top:165px"><div class="tile-fill" role="img" aria-label="External battery wiring" style="background:linear-gradient(150deg,#7d8487,#b8443f 50%,#dfe2e3)"></div></div>
  <div class="tile" style="left:372px;top:165px"><div class="tile-fill" role="img" aria-label="Transformer system panel" style="background:linear-gradient(150deg,#b5a07a,#7c5b3f 55%,#e7e0d4)"></div></div>
  <div class="tile-label" style="left:14px;top:283px">Rackmount type UPS</div>
  <div class="tile-label" style="left:128px;top:283px">Modular type UPS</div>
  <div class="tile-label" style="left:245px;top:283px">External battery<br>type UPS</div>
  <div class="tile-label" style="left:361px;top:283px">Transformer<br>system</div>

  <h2 class="sec-title" style="left:27px;top:342px">Server Room Setup &nbsp;(CRAC)</h2>
  <p class="body" style="left:29px;top:386px;width:442px">Cooling System is a vital part of a data center. How well the cooling capacity you estimated and how accurate the resources you request from your building ensure the uptime of your data center, endurance of server data, and durableness of the business being supported.</p>

  <div class="tile" style="left:25px;top:469px"><svg width="92" height="94" viewBox="0 0 92 94" fill="none" stroke="#444" stroke-width="2"><path d="M18 38h34M16 46h40M18 54h34M20 62h30"/><circle cx="62" cy="40" r="5"/><circle cx="66" cy="58" r="5"/></svg></div>
  <div class="tile" style="left:139px;top:469px"><svg width="92" height="94" viewBox="0 0 92 94" fill="none" stroke="#444" stroke-width="3"><path d="M18 30q7-7 14 0t14 0t14 0t14 0M18 46q7-7 14 0t14 0t14 0t14 0M18 62q7-7 14 0t14 0t14 0t14 0"/></svg></div>
  <div class="tile" style="left:256px;top:469px"><svg width="92" height="94" viewBox="0 0 92 94" fill="none" stroke="#444" stroke-width="2"><rect x="18" y="30" width="56" height="34"/><rect x="26" y="36" width="40" height="22"/><path d="M34 36v22M46 36v22M58 36v22"/></svg></div>
  <div class="tile" style="left:372px;top:469px"><svg width="92" height="94" viewBox="0 0 92 94" fill="none" stroke="#444" stroke-width="2"><path d="M46 14v12M20 30h52"/><rect x="22" y="36" width="12" height="26"/><rect x="40" y="36" width="12" height="26"/><rect x="58" y="36" width="12" height="26"/><path d="M18 66h56"/></svg></div>
  <div class="tile-label" style="left:14px;top:587px">Air cooled type</div>
  <div class="tile-label" style="left:128px;top:587px">Chilled water type</div>
  <div class="tile-label" style="left:245px;top:587px">Wall-mount type</div>
  <div class="tile-label" style="left:361px;top:587px">Ceiling-mount type</div>

  <h2 class="sec-title" style="left:500px;top:44px">All-in-One Rack Solution (Key</h2>
  <div class="brand" style="left:846px;top:42px;font-size:20px"><span class="brand-mark" style="width:18px;height:18px"></span>Vantaro</div>
  <div class="abs" style="left:500px;top:95px;width:471px;height:289px;background:var(--green)"></div>
  <div class="abs" role="img" aria-label="Rows of server racks lit in blue and red" style="left:516px;top:95px;width:455px;height:273px;background:linear-gradient(120deg,#0b1f3f,#1b4f9a 45%,#6a1d3a 75%,#0c1a33)"></div>
  <p class="body" style="left:537px;top:428px;width:396px">All-in-one rack enclosure is a new approach of rack providing a self-contained ecosystem to accommodate servers and devices. It itself already contained modular cooling, fire suppression, backup power, PDU, remote monitoring and infrastructure management tool.</p>
  <p class="body" style="left:537px;top:510px;width:396px">With its pre-configured module, it is a perfect partner to commercials who has little space for their IT device, temp or remote office and who needs speedy deployment. Plus its perfect plug-play design, it can be easily relocated and reinstalled in a new location with only minimal expenses.</p>

  <div class="footer-band" style="left:0;width:486px;height:36px;background:linear-gradient(90deg,var(--teal-dark),var(--teal))"></div>
  <div class="footer-band" style="left:486px;width:485px;height:52px;background:linear-gradient(90deg,var(--teal),var(--teal-dark))"></div>
  <div class="pg" style="left:24px">01</div>
  <div class="url" style="left:67px">www.vantarotech.example</div>
  <div class="url" style="right:60px">www.vantarotech.example</div>
  <div class="pg" style="right:0">02</div>
</section>

<!-- Spread: pages 03-04 -->
<section class="page spread" style="left:115px;top:2222px;width:992px;height:704px">
  <h2 class="sec-title" style="left:25px;top:46px">Structured Cabling and Fiber Backbone Wiring</h2>
  <div class="abs" style="left:0;top:82px;width:494px;height:290px;background:var(--teal)"></div>
  <p class="body" style="left:25px;top:106px;width:442px;color:#fff">Structured cabling is the design and installation of a cabling systems that will support multiple hardware uses systems and be suitable for today's needs and those of the future. We deliver robust structured cabling systems that are equipped to accommodate a multitude of applications including voice, data, video, security, and etc.</p>
  <p class="body" style="left:25px;top:236px;width:175px;color:#fff">From the walk through to cable design and installation, we ensure your entire project is completed with minimal interruption, utilising best practices, delivered on time, and within budget.</p>
  <div class="abs" role="img" aria-label="Blue patch cables in a network panel" style="left:228px;top:195px;width:213px;height:136px;border:4px solid var(--green);background:linear-gradient(135deg,#0a1a3a,#2e5fc8 50%,#0d1f44)"></div>

  <div class="brand" style="left:194px;top:428px;font-size:22px"><span class="brand-mark" style="width:20px;height:20px"></span>Vantaro</div>
  <h2 class="sec-title" style="left:106px;top:480px">Structured Cabling Partners</h2>
  <div class="partner" style="left:36px;top:558px;width:150px;height:40px"></div>
  <div class="partner" style="left:212px;top:548px;width:132px;height:70px"></div>
  <div class="partner" style="left:380px;top:540px;width:94px;height:90px"></div>

  <h2 class="sec-title" style="left:511px;top:44px">Other Solution (CCTV &amp; Access Control<br>Solution, Conference Room AV Solution)</h2>
  <p class="body" style="left:511px;top:118px;width:445px">Digital &amp; Video surveillance (CCTV/DVR) plays a significant role in overall security systems. With real time monitoring of your office or particular areas, potential intrusion can be detected or reported before they happen; allowing you to take a preventive or proactive approach to your security operations.</p>
  <p class="body" style="left:511px;top:187px;width:445px">No matter if you required to use a hybrid analogue plus IP or a pure IP system, we can tailor a durable and expandable solution to cope with your business needs.</p>
  <p class="body" style="left:511px;top:228px;width:445px">Vantaro design and implement access control solutions that fits office facilities and restricted areas like data center. Advanced technologies bring you the functionality you need with expandability for the future.</p>
  <p class="body" style="left:511px;top:283px;width:445px">With multiple combination of use of means of access, cards, finger-prints and facial recognition; organisations not only can monitor attendance but only ensure the highest level of security for special areas. No worries for multiple offices! We can tie them together to ease and automate the overall management.</p>
  <p class="body" style="left:511px;top:366px;width:445px">Conference Room is a place putting together multimedia presentation technology, video and audio conferencing systems, interactive communication products and centralised integrated management systems. Vantaro Technology as a leading IT &amp; AV system integrator offers a wide range of different audiovisual solutions based on your need. With our field engineer's extensive knowledge in not only AV, but also network and IP, overall project is simplified and project life cycle are well shortened.</p>
  <div class="abs" role="img" aria-label="Bright conference room with a wall screen and glass partition" style="left:530px;top:455px;width:462px;height:193px;background:linear-gradient(180deg,#f4f5f5,#c9cccd 55%,#8e9394)"></div>

  <div class="footer-band" style="left:0;width:496px;height:40px;background:linear-gradient(90deg,var(--teal-dark),var(--teal))"></div>
  <div class="footer-band" style="left:496px;width:496px;height:40px;background:linear-gradient(90deg,var(--teal),var(--teal-dark))"></div>
  <div class="pg" style="left:24px">03</div>
  <div class="url" style="left:68px">www.vantarotech.example</div>
  <div class="url" style="right:60px">www.vantarotech.example</div>
  <div class="pg" style="right:0">04</div>
</section>

</body>
</html>
```